Design a single about page website landing page

I need a new about page design required for a WORDPRESS agency site - Matte Look effect, use of illustration and high-res 4k images. I am in the process of launching a new start-up focussed digital agency. Must be easy for the developer to integrate into Wordpress CMS.

I can show you what the existing site looks like (please find attached).
Please also take a look at two draft rough examples (I've created, not happy with either of these but should give you an idea of what I'm trying to achieve).

The about page design needs to tell the story of the textual content which I will also supply (please find attached), the page design needs to compliment the service page while giving a completely different experience to the service pages (I want the user experience to be different on this page).

Target Market(s)

Specialist Digital Marketing Consultancy

Font styles to use
Sans Serif

Requirements
Must have
• (o) Different user experience to other pages of the site (but complimentary)
this is a company about page so it has to be engaging
(o) Matte Look effect
(o) Use of illustration
(o) High-res images

```html
<!DOCTYPE html>
<html lang="en">
<head>
<meta charset="utf-8">
<title>About Us – Vantix</title>
<link href="https://fonts.googleapis.com/css2?family=Open+Sans:wght@400;600;700&family=Lato:wght@300;400;700&display=swap" rel="stylesheet">
<style>
:root{
  --green:#4f9d54;
  --green-soft:#edf3ec;
  --ink:#111111;
  --text:#3a3a3a;
  --grey-band:#f6f6f6;
  --line:#e6e6e6;
  --footer:#0c0c0c;
  --footer-bar:#050505;
  --footer-text:#d6d6d6;
}
*{margin:0;padding:0;box-sizing:border-box}
html,body{width:1200px;height:2558px;overflow:hidden;background:#fff}
body{position:relative;font-family:"Lato",sans-serif;color:var(--text)}
.abs{position:absolute}

/* header */
.site-header{left:0;top:0;width:1200px;height:89px;border-bottom:1px solid var(--line);background:#fff}
.brand{left:90px;top:26px;font-family:"Open Sans",sans-serif;font-weight:700;font-size:26px;color:var(--ink);letter-spacing:-0.5px;display:flex;align-items:center;gap:4px}
.brand .dot{width:7px;height:7px;border-radius:50%;background:var(--green);margin-top:16px}
.main-nav{right:82px;top:27px;display:flex;align-items:center;font-family:"Open Sans",sans-serif;font-weight:600;font-size:14px;color:var(--ink)}
.main-nav a{color:inherit;text-decoration:none;padding:8px 17px;border-radius:3px;margin-left:6px}
.main-nav a.active{background:var(--green);color:#fff}
.main-nav .caret{font-size:10px}

/* breadcrumb */
.page-band{left:0;top:89px;width:1200px;height:102px;background:var(--grey-band);border-bottom:1px solid var(--line)}
.page-title{left:91px;top:128px;display:flex;align-items:center;gap:10px;font-family:"Open Sans",sans-serif;font-weight:700;font-size:22px;color:var(--ink)}

/* hero */
.hero-title{left:0;top:266px;width:1200px;text-align:center;font-family:"Open Sans",sans-serif;font-weight:700;font-size:47px;color:var(--ink)}
.hl{color:var(--green)}
.hero-sub{left:0;top:333px;width:1200px;text-align:center;font-family:"Open Sans",sans-serif;font-size:20px;color:#222}

/* sections */
.art{border-radius:6px}
.sec-heading{font-family:"Open Sans",sans-serif;font-weight:700;font-size:29px;color:var(--ink);white-space:nowrap}
.rule{height:3px;width:80px;background:var(--green)}
.copy p{font-size:17px;line-height:24px;margin-bottom:16px;color:var(--text)}
.service-band{left:0;top:910px;width:1200px;height:445px;background:var(--green-soft)}

/* challenge */
.challenge{left:0;top:2055px;width:1200px;text-align:center;font-family:"Open Sans",sans-serif;font-weight:700;font-size:43px;color:var(--ink)}
.challenge .hl{border-bottom:2px solid var(--green);padding:0 10px 0 0}

/* footer */
.site-footer{left:0;top:2222px;width:1200px;height:336px;background:var(--footer)}
.touch-tab{left:107px;top:2203px;width:185px;height:45px;background:var(--green)}
.foot-head{font-size:20px;color:#fff;font-weight:400}
.foot-about{left:90px;top:2326px;width:560px}
.foot-about p{margin-top:14px;font-size:15px;line-height:25px;color:var(--footer-text);font-weight:300}
.foot-contact{left:785px;top:2326px}
.mail-row{margin-top:18px;display:flex;align-items:center;gap:10px;font-size:15px;color:var(--footer-text)}
.mail-row b{color:#fff;font-weight:700}
.socials{margin-top:16px;display:flex;gap:4px;margin-left:3px}
.socials span{width:32px;height:32px;border-radius:50%;background:#fff;display:block}
.to-top{left:1099px;top:2495px;width:44px;height:44px;background:var(--green);border-radius:3px;display:flex;align-items:center;justify-content:center}
.foot-bar{left:0;top:2515px;width:1200px;height:43px;background:var(--footer-bar)}
.foot-brand{left:90px;top:2527px;font-family:"Open Sans",sans-serif;font-weight:700;font-size:18px;color:#fff}
.copyright{left:188px;top:2531px;font-size:13px;color:var(--footer-text);font-weight:300}
</style>
</head>
<body>

<header class="site-header abs">
  <div class="brand abs">VANTIX<span class="dot"></span></div>
  <nav class="main-nav abs">
    <a class="active" href="#">ABOUT US</a>
    <a href="#">CONSULTANCY</a>
    <a href="#">SERVICES <span class="caret">&#8964;</span></a>
    <a href="#">CONTACT US</a>
  </nav>
</header>

<div class="page-band abs"></div>
<h1 class="page-title abs">
  <svg width="26" height="22" viewBox="0 0 26 22" aria-hidden="true"><path d="M13 1 L25 11 H21 V21 H15.5 V14 H10.5 V21 H5 V11 H1 Z" fill="#4f9d54"/></svg>
  ABOUT US
</h1>

<h2 class="hero-title abs">Our Logic Will <span class="hl">Fuel</span> Your Growth</h2>
<p class="hero-sub abs">Specialist, Results-Driven Digital Solutions Provider</p>

<!-- right place -->
<div class="art abs" role="img" aria-label="Illustration of a team assembling a website layout on a large browser window among green leaves" style="left:90px;top:445px;width:492px;height:390px;background:linear-gradient(135deg,#e3ecf9 0%,#d4e1f6 50%,#e4f0e3 100%)"></div>
<h3 class="sec-heading abs" style="left:648px;top:472px">You’ve Come To The <span class="hl">Right</span> Place</h3>
<div class="rule abs" style="left:612px;top:517px"></div>
<div class="copy abs" style="left:648px;top:532px;width:472px">
  <p>We love to solve problems, be it small or highly-complex, especially those that require a need to Innovate and accelerate business growth through integrated digital solutions.</p>
  <p>We’re not pitching the same plan to every potential client who get’s in touch. We custom-build highly effective digital solutions for every company that works with us based on their goals and we do this by only working with a handful of clients to keep our service standards high.</p>
  <p>We aim to delight clients and their customers with memorable, immersive digital experiences.</p>
</div>

<!-- service box -->
<div class="service-band abs"></div>
<h3 class="sec-heading abs" style="left:90px;top:1015px">What’s In the <span class="hl">Service</span> Box?</h3>
<div class="rule abs" style="left:54px;top:1060px"></div>
<div class="copy abs" style="left:90px;top:1075px;width:466px">
  <p>Naturally, it says on the tin that we deliver the results that our clients seek.</p>
  <p>Ultimately, by working with Us you will be inspired to re-imagine what is possible and create an improved digital journey withEndless possibilities; increasing your ‘bottom line’ and creating efficiencies along the way.</p>
</div>
<div class="art abs" role="img" aria-label="Isometric illustration of a warehouse worker beside green shelving stacked with cardboard boxes and pallets" style="left:620px;top:935px;width:505px;height:490px;background:linear-gradient(160deg,#f1e1cb 0%,#ecdcc7 55%,#e5ece4 100%)"></div>

<!-- fuel growth -->
<div class="art abs" role="img" aria-label="Illustration of a rocket launching above clouds" style="left:90px;top:1505px;width:515px;height:460px;background:linear-gradient(180deg,#6aae6e 0%,#8dbf90 100%)"></div>
<h3 class="sec-heading abs" style="left:648px;top:1496px">Our Logic Will <span class="hl">Fuel</span> Your Growth</h3>
<div class="rule abs" style="left:612px;top:1541px"></div>
<div class="copy abs" style="left:648px;top:1556px;width:472px">
  <p>Logic, methodology, and efficiency are the core of our agency. Our logic dictates our actions, we ask why, we run through scenarios, we think through the process and the take time to understand the details of your business.</p>
  <p style="margin-bottom:0">We are methodical in our approach. Marketing is an investment for our clients, With logical thinking and a methodical approach we ensure the best return on that investment.</p>
  <p>We don't ‘sell’ services, instead, we provide unique solutions to mitigate real businesschallenges, we look at your unique business and craft solutions to solve your problems.Whether that be getting your more visibility</p>
  <p>online, generating traffic, creating an optimised user journey for your customers, keeping existing customers happy; whatever challenge your facing we have the right solution to solve it.</p>
</div>

<h2 class="challenge abs">What’s your <span class="hl">business challenge?</span></h2>

<!-- footer -->
<footer>
  <div class="site-footer abs"></div>
  <div class="touch-tab abs" role="img" aria-label="Hand-lettered ‘Get in Touch!’ tab"></div>
  <div class="foot-about abs">
    <h4 class="foot-head">About</h4>
    <p>Brightpath Media is a digital marketing advisory partner and services consultancy, passionate about all thing’s digital. Focussed on delivering exceptional strategic, targeted and creative solutions.</p>
  </div>
  <div class="foot-contact abs">
    <h4 class="foot-head">Contact</h4>
    <div class="mail-row">
      <svg width="18" height="13" viewBox="0 0 18 13" aria-hidden="true"><rect width="18" height="13" rx="1" fill="#6b6b6b"/><path d="M1 1 L9 7 L17 1" stroke="#0c0c0c" stroke-width="1.5" fill="none"/></svg>
      <span><b>Email:</b> hello@brightpathmedia.com</span>
    </div>
    <div class="socials"><span></span><span></span><span></span><span></span></div>
  </div>
  <div class="foot-bar abs"></div>
  <div class="to-top abs">
    <svg width="14" height="9" viewBox="0 0 14 9" aria-hidden="true"><path d="M1 8 L7 2 L13 8" stroke="#fff" stroke-width="2" fill="none"/></svg>
  </div>
  <div class="foot-brand abs">VANTIX</div>
  <p class="copyright abs">© Copyright Brightpath Media. All Rights Reserved.</p>
</footer>

</body>
</html>
```